Upscale business cards needed for family office

We would like professional business cards created for employees of our family office. Relatively simple and straightforward, but also with a unique element to set them apart. Probably stick with neutral and simple colors that mesh well with the colors in the logo. We need space for the traditional elements, including name, title, address, email/phone number.

Industry/Entity Type

Business

Contact Information for Business Card

Space for name, title, phone number, email, address

```html
<!DOCTYPE html>
<html lang="en">
<head>
<meta charset="utf-8">
<title>Northmere Business Card</title>
<link rel="stylesheet" href="https://fonts.googleapis.com/css2?family=Open+Sans:wght@400;600;700&display=swap">
<style>
  :root {
    --backdrop: #4a3e3a;
    --card: #141516;
    --card-edge: #1d1e20;
    --accent: #1e9fd6;
    --text-light: #e6e6e6;
    --text-muted: #9a9c9f;
    --rule: #8d8f92;
    --mark-frame: #c9cbce;
    --mark-fill: #f2f2f2;
    --mark-ink: #4d5257;
  }
  * { margin: 0; padding: 0; box-sizing: border-box; }
  html, body {
    width: 1200px; height: 864px; overflow: hidden;
    background: var(--backdrop);
    font-family: "Open Sans", Arial, sans-serif;
  }
  .canvas { position: relative; width: 1200px; height: 864px; }

  .card {
    position: absolute;
    width: 520px; height: 298px;
    background: var(--card);
    border: 1px solid var(--card-edge);
    box-shadow: 0 10px 26px rgba(0,0,0,.45);
  }

  /* Front */
  .card-front { left: 70px; top: 110px; }
  .front-brand {
    position: absolute; left: 140px; top: 86px;
    display: flex; align-items: center; gap: 14px;
  }
  .brand-square {
    width: 30px; height: 30px;
    background: var(--accent);
  }
  .brand-name {
    font-size: 34px; font-weight: 600; letter-spacing: 1px;
    color: var(--text-muted);
  }
  .front-web {
    position: absolute; left: 0; right: 0; top: 190px;
    text-align: center;
    font-size: 13px; letter-spacing: 5px;
    color: var(--text-muted);
  }

  /* Back */
  .card-back { left: 610px; top: 456px; }
  .person {
    position: absolute; left: 34px; top: 44px;
  }
  .person-name {
    font-size: 19px; font-weight: 700; letter-spacing: .5px;
    color: var(--accent);
  }
  .person-title {
    font-size: 14px; color: var(--accent); margin-top: -2px;
  }
  .contact-list {
    position: absolute; left: 34px; top: 106px;
    list-style: none;
  }
  .contact-list li {
    display: flex; align-items: center; gap: 12px;
    height: 22px;
    font-size: 13px; color: var(--text-light);
  }
  .contact-list svg { width: 14px; height: 14px; flex: none; }
  .contact-rule {
    position: absolute; left: 34px; right: 34px; top: 182px;
    height: 1px; background: var(--rule);
  }
  .back-brand {
    position: absolute; right: 34px; top: 40px;
    width: 140px; height: 120px;
    background: var(--mark-fill);
    border: 3px solid var(--mark-frame);
    display: flex; flex-direction: column;
    align-items: center; justify-content: center; gap: 10px;
  }
  .back-brand .brand-square { width: 20px; height: 20px; }
  .back-brand .brand-name {
    font-size: 19px; color: var(--mark-ink); letter-spacing: .5px;
  }
  .address {
    position: absolute; right: 34px; bottom: 30px;
    text-align: right;
    font-size: 14px; line-height: 21px;
    color: var(--text-light);
  }
</style>
</head>
<body>
<main class="canvas">

  <section class="card card-front" aria-label="Card front">
    <div class="front-brand">
      <span class="brand-square"></span>
      <span class="brand-name">Northmere</span>
    </div>
    <p class="front-web">www.northmere.com</p>
  </section>

  <section class="card card-back" aria-label="Card back">
    <div class="person">
      <p class="person-name">MARTIN HALE</p>
      <p class="person-title">President</p>
    </div>

    <ul class="contact-list">
      <li>
        <svg viewBox="0 0 16 16" aria-hidden="true"><path fill="var(--accent)" d="M3.5 1.5l2.6 0 1 3.2-1.6 1.2a8 8 0 0 0 4.6 4.6l1.2-1.6 3.2 1v2.6c0 .8-.7 1.5-1.5 1.5C6.9 14 2 9.1 2 3c0-.8.7-1.5 1.5-1.5z"/></svg>
        555 0142 7789
      </li>
      <li>
        <svg viewBox="0 0 16 16" aria-hidden="true"><rect x="1" y="3" width="14" height="10" fill="var(--accent)"/><path d="M1.5 3.5L8 9l6.5-5.5" fill="none" stroke="var(--card)" stroke-width="1.3"/></svg>
        martin@northmere.com
      </li>
      <li>
        <svg viewBox="0 0 16 16" aria-hidden="true"><path fill="var(--accent)" d="M8 1a5 5 0 0 0-5 5c0 3.6 5 9 5 9s5-5.4 5-9a5 5 0 0 0-5-5z"/><circle cx="8" cy="6" r="1.8" fill="var(--card)"/></svg>
        www.northmere.com
      </li>
    </ul>

    <div class="contact-rule"></div>

    <div class="back-brand">
      <span class="brand-square"></span>
      <span class="brand-name">Northmere</span>
    </div>

    <p class="address">2710 Alder Crest Lane<br>Lake Haven, NY 11020</p>
  </section>

</main>
</body>
</html>
```